Verpackungsdesign für italienische Produkte gesucht
Die Zusammenarbeit mit dem Designer 7Pixo hat sehr viel Spaß gemacht. Jeder Änderungswunsch wurde super schnell in die Tat umgesetzt. Die Kommunikation verlief reibungslos. Das Ergebnis ist einfach klasse geworden. Er hat ein großes Talent für den Entwurf von Designs. Ich freue mich sehr darauf, auch zukünftige Projekte mit ihm durchführen zu können. Vielen Dank nochmal an Ihn für die tolle Arbeit und die Unterstützung. Ich kann eine Zusammenabeit mit dem Designer 7Pixo nur empfehlen.
Zielgruppe
Liebe Designerinnen und Designer,
wir sind ein Unternehmen, welches Olivenöl, Pasta und Wein sowie Olivenblättertee und Tomatensoße auf Sizilien (Italien) in Gibellina produziert. In vierter Generation produziert die Familie Lorusso landwirtschaftliche Erzeugnisse, die nach biologischen Prinzipien angebaut werden. Im Ackerbau verzichten wir auf synthetisch hergestellte Pflanzenschutzmittel, Mineraldünger und Grüne Gentechnik. Da in der heutigen Zeit viele Konsumenten den Ursprung der gekauften Produkte nicht mehr zurückverfolgen können und ihnen in dieser Hinsicht kaum Transparenz gewährleistet wird, möchten wir im Namen der Familie Lorusso unseren Kunden den Herstellungsprozess vom Anbau bis zur Fertigstellung des Enderzeugnisses transparent aufzeigen und sie für die bewusste und gesunde Ernährung sensibilisieren.
Unsere Zielgruppe sind ernährungsbewusste Personen, überwiegend Frauen im mittleren Alter, die auf bewusste, gesunde Ernährung viel Wert legen.
Vielen lieben Dank für eure Arbeit im Voraus. Ich freue mich sehr auf die Designvorschläge.
Lieben Gruß
Marta & Carlo Lorusso
Aufgabenstellung
KREATIVE DESIGNER gesucht
WIR SUCHEN EIN VERPACKUNGSKONZEPT FÜR UNSERE PRODUKTE
Für unsere Produkte: Olivenöl, Pasta und Wein sowie Olivenblättertee und Tomatensoße benötigen wir ein Verpackungsdesign, welches erkennen lässt, dass die Produkte zu einer Produktfamilie gehören. Darüber hinaus benötigen wir das Design für den Kartonanhänger, der an jedes unserer Produkte ran gehängt werden soll.
Erst einmal suchen wir nach Vorschlägen für ein Verpackungsdesign. Im Anschluss an dieses Projekt würden wir gerne mit dem Designer die Reinzeichnungen fertig erstellen. Den Preis für die Reinzeichnung würden wir dann gerne mit dem Designer verhandeln.
Mit dem Designer, der das Projekt gewinnt, streben wir auch nach dem Produktende eine enge Zusammenarbeit an, da sich unser Produktportfolio stetig erweitern wird und Folgeaufträge bereits in Planung sind.
Für die Produkte Olivenöl, Pasta und Tee sowie Tomatensoße benötigen wir Etiketten mit Vorder- und Rückseite. Für die Pasta-Verpackung soll ein Design für den Kartonreiter aus dünnem Kartonpapier erstellt werden (siehe Bild Pasta Design Beispiel). Dieses Kartonpapier könnte schwarz sein, da die Olivenölflasche, die Weinflaschen sowie die Verpackung für Tee und die Flasche für Tomatensoße ebenfalls dunkel sind.
Das Design sollte elegant und qualitativ hochwertig aussehen. Mit unseren Produkten sollen die folgenden Werte transportiert werden: Tradition, Familie, hochwertige Qualität, Transparenz, biologischer Anbau, bewusste Ernährung, Liebe zum Produkt, Sizilien,
Es sollten max. 4 verschiedene Farben verwendet werden.
In der Datei Vorgaben zum Design stehen weitere Angaben. Zusätzlich besteht eine PDF Datei mit Bildern zur Gestaltungshilfe. Eine weitere Datei besteht mit allen Verpackungen, die gestaltet werden sollen.
Alle Logos sind auch noch in weiteren Formaten verfügbar.
Vielen Dank im Voraus
Marta & ..

```html
<!DOCTYPE html>
<html lang="de">
<head>
<meta charset="utf-8">
<title>Lorusso – Bio-Natives Olivenöl Extra Etikett</title>
<link rel="stylesheet" href="https://fonts.googleapis.com/css2?family=Oswald:wght@200;300;400&display=swap">
<style>
  :root {
    --stage: #e6e6e6;
    --paper: #ffffff;
    --olive-green: #cbd98f;
    --gold: #d6ad45;
    --ink: #3a3a3a;
    --tile-light: #e4ecf6;
    --tile-sky: #b7cce8;
    --tile-blue: #7fa3cf;
    --tile-sand: #eadfb6;
    --line: #222222;
  }
  * { margin: 0; padding: 0; box-sizing: border-box; }
  html, body {
    width: 849px;
    height: 1200px;
    overflow: hidden;
    background: var(--stage);
  }
  .canvas {
    position: relative;
    width: 849px;
    height: 1200px;
    font-family: "Oswald", sans-serif;
  }
  .label {
    position: absolute;
    left: 104px;
    top: 240px;
    width: 640px;
    height: 722px;
    overflow: hidden;
  }
  .label__tiles {
    position: absolute;
    inset: 0;
    background: linear-gradient(135deg,
      var(--tile-light) 0%,
      var(--tile-sky) 35%,
      var(--tile-blue) 55%,
      var(--tile-sky) 75%,
      var(--tile-sand) 100%);
  }
  .brand-box {
    position: absolute;
    left: 247px;
    top: 46px;
    width: 151px;
    height: 143px;
    background: var(--paper);
    border: 1.5px solid var(--line);
    display: flex;
    flex-direction: column;
    align-items: center;
    justify-content: flex-end;
    padding-bottom: 14px;
  }
  .brand-box__dot {
    width: 44px;
    height: 44px;
    border-radius: 50%;
    background: var(--gold);
    margin-bottom: 14px;
  }
  .brand-box__name {
    font-weight: 400;
    font-size: 24px;
    letter-spacing: 2px;
    line-height: 1;
    color: var(--gold);
  }
  .product-panel {
    position: absolute;
    left: 154px;
    top: 235px;
    width: 348px;
    height: 358px;
    background: var(--paper);
    border: 1.5px solid var(--line);
    text-align: center;
    color: var(--olive-green);
  }
  .product-panel__title {
    position: absolute;
    left: 0;
    right: 0;
    top: 10px;
    font-weight: 200;
    font-size: 66px;
    line-height: 76px;
    letter-spacing: 0;
  }
  .product-panel__origin {
    position: absolute;
    left: 0;
    right: 0;
    top: 247px;
    font-weight: 300;
    font-size: 20px;
    line-height: 26px;
  }
  .product-panel__volume {
    position: absolute;
    left: 0;
    right: 0;
    top: 309px;
    font-weight: 300;
    font-size: 22px;
    line-height: 28px;
    color: var(--ink);
  }
  .social-strip {
    position: absolute;
    left: 173px;
    bottom: 4px;
    width: 294px;
    height: 34px;
    background: var(--paper);
    display: flex;
    align-items: center;
    justify-content: center;
    gap: 9px;
    font-weight: 300;
    font-size: 15px;
    color: var(--ink);
  }
  .social-strip__mark {
    width: 20px;
    height: 20px;
    background: var(--olive-green);
    border-radius: 4px;
  }
</style>
</head>
<body>
  <main class="canvas">
    <section class="label">
      <div class="label__tiles" role="img" aria-label="Sizilianisches Majolika-Fliesenmuster in Blau, Türkis, Gelb und Weiß"></div>

      <div class="brand-box">
        <span class="brand-box__dot"></span>
        <span class="brand-box__name">LORUSSO</span>
      </div>

      <div class="product-panel">
        <h1 class="product-panel__title">BIO-NATIVES<br>OLIVENÖL<br>EXTRA</h1>
        <p class="product-panel__origin">D.O.P. VALLE DEL BELICE</p>
        <p class="product-panel__volume">500ML</p>
      </div>

      <div class="social-strip">
        <span>FOLGEN SIE UNS:</span>
        <span class="social-strip__mark"></span>
        <span>FAM.LORUSSO</span>
      </div>
    </section>
  </main>
</body>
</html>
```